Website for Company to help with House Restoration from Hurricane Damage

Crisp, Clean and Professional!

I need a FRONT page for a website. I need it created in photoshop with the layers intact. We DO NOT need the HTML or DRB for the site. Simply the design. Any fonts you use will need to be included if they are not standard. Please make sure any fonts you use in the body of the text are available for use on Google Fonts.

I have attached a word doc that lists the menu items and additional instructions.

A little about the company - after Hurricane Marlow - DRB developed a system which allows the house to be raised, the Tremlets installed, and the house reset on the Tremlets without the expense of moving the house or driving new pilings. This option can be installed in a matter of days with limited space and at a lower construction cost.

Please refer to the attached musthaves.doc and images that are included.

The main page must incorporate the menu, the attached photos w/ text underneath (text is in the word doc attached), and the text included in the word doc.

Standard footer with contact info as well.

If you have questions please contact us!
Updates

Designs are due by Friday! We will pick one this weekend.  We are unable to change it from 10 days to 5.  Thank you!!!

Target Market(s)

People who lost their homes or businesses due to a hurricane.

Industry/Entity Type

Construction

Requirements
Must have
• See attached musthaves.doc

```html
<!DOCTYPE html>
<html lang="en">
<head>
<meta charset="utf-8">
<title>Dune Ridge Building Systems, LLC</title>
<link href="https://fonts.googleapis.com/css2?family=Quattrocento:wght@400;700&family=Quattrocento+Sans&display=swap" rel="stylesheet">
<style>
  :root {
    --olive: #76874f;
    --olive-dark: #5f7040;
    --olive-text: #6a7f45;
    --sage: #c3d29c;
    --sage-deep: #9fb173;
    --header-top: #c7d6a4;
    --ink: #1d1d1d;
    --muted: #8a8a8a;
    --card-bg: #f4f4f4;
    --card-line: #dcdcdc;
    --link-red: #c0191b;
    --white: #ffffff;
  }
  * { box-sizing: border-box; margin: 0; padding: 0; }
  html, body { width: 1200px; height: 1178px; overflow: hidden; background: var(--white); }
  body { font-family: "Quattrocento", serif; color: var(--ink); position: relative; }

  .site-header {
    position: absolute; left: 0; top: 0; width: 1200px; height: 131px;
    border-top: 4px solid #111;
    background: linear-gradient(to bottom, var(--header-top), var(--white));
  }
  .brand { position: absolute; left: 154px; top: 14px; display: flex; align-items: center; gap: 12px; height: 104px; }
  .brand-mark { width: 86px; height: 86px; border-radius: 50%; background: var(--olive); }
  .brand-name { font-family: "Quattrocento", serif; font-weight: 700; font-size: 36px; color: var(--olive-text); margin-top: 26px; }
  .header-phone {
    position: absolute; right: 154px; top: 22px; display: flex; align-items: center; gap: 4px;
    font-weight: 700; font-size: 23px; color: var(--olive-text);
  }

  .main-nav {
    position: absolute; left: 0; top: 131px; width: 1200px; height: 39px; background: var(--olive);
  }
  .main-nav ul { list-style: none; display: flex; position: absolute; left: 153px; top: 0; height: 39px; align-items: center; }
  .main-nav li { color: var(--white); font-size: 13.5px; letter-spacing: 0.2px; margin-right: 33px; }
  .main-nav li:nth-child(5) { margin-right: 38px; }

  .hero {
    position: absolute; left: 136px; top: 171px; width: 928px; height: 364px;
    background: linear-gradient(to bottom, #8d84a0 0%, #d59aa6 30%, #e9b7a8 42%, #7a7388 58%, #9e8c93 75%, #c8b3ad 100%);
  }
  .welcome-band {
    position: absolute; left: 136px; top: 535px; width: 928px; height: 60px;
    background: linear-gradient(to bottom, #d8d8d8, var(--white));
  }

  .intro { position: absolute; left: 154px; top: 564px; width: 892px; }
  .intro h1 { font-weight: 400; font-size: 21px; color: #111; margin-bottom: 8px; }
  .intro h1 span { color: var(--olive-text); }
  .intro p { font-size: 13px; line-height: 18.1px; text-align: justify; margin-bottom: 18px; }

  .features { position: absolute; left: 154px; top: 806px; width: 892px; display: flex; justify-content: space-between; }
  .feature { width: 285px; height: 198px; background: var(--card-bg); border: 1px solid var(--card-line); border-radius: 4px; overflow: hidden; text-align: center; }
  .feature-title {
    height: 66px; background: linear-gradient(to bottom, var(--olive), var(--olive-dark));
    color: var(--white); font-weight: 700; font-size: 19px; line-height: 22px;
    display: flex; align-items: center; justify-content: center; padding: 0 6px;
  }
  .feature-text { color: var(--muted); font-size: 13.5px; line-height: 21.5px; padding: 11px 16px 0; height: 98px; overflow: hidden; }
  .feature-link { display: inline-flex; align-items: center; gap: 4px; font-family: "Quattrocento Sans", sans-serif; font-weight: 700; font-size: 9.5px; color: var(--link-red); margin-top: 8px; }

  .site-footer { position: absolute; left: 0; top: 1025px; width: 1200px; height: 124px; background: var(--sage); }
  .contact { position: absolute; left: 154px; top: 8px; }
  .contact h2, .social h2 { font-weight: 400; font-size: 24px; color: #222; margin-bottom: 6px; }
  .contact p { font-size: 13px; line-height: 18.2px; color: #111; }
  .social { position: absolute; right: 154px; top: 8px; text-align: right; }
  .social-icons { display: flex; gap: 4px; justify-content: flex-end; margin-top: 6px; }
  .social-icons span { width: 36px; height: 39px; background: var(--olive); display: block; }
  .copyright {
    position: absolute; left: 0; top: 1149px; width: 1200px; height: 29px; background: var(--sage-deep);
    font-family: "Quattrocento Sans", sans-serif; font-size: 9.5px; color: #eef2e2; letter-spacing: 0.4px;
    display: flex; align-items: center; justify-content: center;
  }
</style>
</head>
<body>
  <header class="site-header">
    <div class="brand">
      <div class="brand-mark"></div>
      <div class="brand-name">Dune Ridge Building Systems</div>
    </div>
    <div class="header-phone">
      <svg width="28" height="22" viewBox="0 0 28 22" aria-hidden="true">
        <path d="M2 8 Q14 -2 26 8 L23 11 L19 8 L9 8 L5 11 Z" fill="#555"/>
        <rect x="6" y="11" width="16" height="10" rx="2" fill="#555"/>
        <circle cx="14" cy="16" r="3" fill="#ddd"/>
      </svg>
      (555) 014-2287
    </div>
  </header>

  <nav class="main-nav">
    <ul>
      <li>HOME</li>
      <li>SERVICES</li>
      <li>ABOUT US</li>
      <li>PRODUCT SPECIFICATIONS</li>
      <li>DESIGN DOCUMENTATION</li>
      <li>CONTACT US</li>
    </ul>
  </nav>

  <div class="hero" role="img" aria-label="Sunset over a bay with boats on the water and a parent and child on the beach"></div>
  <div class="welcome-band"></div>

  <section class="intro">
    <h1>Welcome to <span>Dune Ridge Building Systems, LLC</span></h1>
    <p>Systems for extending the height of existing piles are not available on today's market.&nbsp; Dune Ridge Building Systems, LLC (DRB) has developed two systems to allow for Piles to be extended that provide superior structural support without corrosion and maintenance concerns.&nbsp; We provided two systems, a complete system, Pile Cap Extension Tremlets, and Pile Splice.&nbsp; These two systems allow a home to be raised to by up to 54", higher extensions possible with additional design consideration for lateral support. Shown below is the full Piling Extension system, which connects to the top of the existing pile. The system modular and can be cut to meet specific needs of the home.</p>
    <p>Our Patented Piling system has been designed to withstand the corrosive environment of beach communities. The salt water and windblown sand corrodes unprotected materials, and yes, even stainless steel. Our system utilizes a high strength carbon fiber material that is corrosion proof from salt water and UV proof.&nbsp; The system will not erode, decay or loose strength over time. The system has three installation conditions, for raising a house on existing pilings, repairing damaged pilings, and for connecting new pilings to floor joists in new construction.</p>
  </section>

  <section class="features">
    <article class="feature">
      <h3 class="feature-title">Raising a house on<br>existing pilings</h3>
      <p class="feature-text">Lorem Ipsum. Proin gravida nibh vel velit auctor aliquet. Aenean sollicitudin, lorem quis bibendum auctor, nisi elit consequat ipsum, nec sagittis sem nibh id elit. Duis</p>
      <span class="feature-link">View more <svg width="14" height="12" viewBox="0 0 14 12"><path d="M1 6 H12 M7 1 L12 6 L7 11" stroke="#222" stroke-width="1.6" fill="none"/></svg></span>
    </article>
    <article class="feature">
      <h3 class="feature-title">Repairing<br>damaged pilings</h3>
      <p class="feature-text">Lorem Ipsum. Proin gravida nibh vel velit auctor aliquet. Aenean sollicitudin, lorem quis bibendum auctor, nisi elit consequat ipsum, nec sagittis sem nibh id elit. Duis</p>
      <span class="feature-link">View more <svg width="14" height="12" viewBox="0 0 14 12"><path d="M1 6 H12 M7 1 L12 6 L7 11" stroke="#222" stroke-width="1.6" fill="none"/></svg></span>
    </article>
    <article class="feature">
      <h3 class="feature-title">Connecting new pilings to<br>floor joists in new construction</h3>
      <p class="feature-text">Lorem Ipsum. Proin gravida nibh vel velit auctor aliquet. Aenean sollicitudin, lorem quis bibendum auctor, nisi elit consequat ipsum, nec sagittis sem nibh id elit. Duis</p>
      <span class="feature-link">View more <svg width="14" height="12" viewBox="0 0 14 12"><path d="M1 6 H12 M7 1 L12 6 L7 11" stroke="#222" stroke-width="1.6" fill="none"/></svg></span>
    </article>
  </section>

  <footer class="site-footer">
    <div class="contact">
      <h2>Contact info</h2>
      <p>Dune Ridge Building Systems, LLC</p>
      <p>PO Box 4410,&nbsp; Harbor Point, PA 19000-0044</p>
      <p>Tel: (555) 014-2287</p>
      <p>Email: sales@duneridgebuilding.com</p>
    </div>
    <div class="social">
      <h2>Lets get social</h2>
      <div class="social-icons">
        <span role="img" aria-label="Social network link"></span>
        <span role="img" aria-label="Social network link"></span>
        <span role="img" aria-label="Social network link"></span>
        <span role="img" aria-label="Social network link"></span>
      </div>
    </div>
  </footer>
  <div class="copyright">Copy © 2013 Dune Ridge Building Systems, LLC. All rights reserved.</div>
</body>
</html>
```